Signage for a foam car wash facility

We need signages done for a foam car wash.
We use only premium, environment-friendly, biodegradable foam wash and cleaning products.
We are in a commercial center (mall) situated in an upscale part of town and need our signage to reflect that.
We need signages for directions (two or three smaller ones), one showing that we are here, and at the actual car wash.
We will provide our logo, the texts, some pictures of the actual location the dimensions of the signages.
We need the signages to be informative, clean, crisp, modern with the use of icons if possible and some colour so that we get the attention of clients passing -by without being too flashy.
Directions to the car wash should look like a petal of a flower directing towards the car wash

Target Market(s)

Upscale market with a school and a gym next to it. Mom and dad's dropping their children at school, offices nearby.

Industry/Entity Type

Car Wash

Requirements
Nice to have
• icons, some colors,Directions to the car wash should look like a petal of a flower directing towards the car wash

```html
<!DOCTYPE html>
<html lang="en">
<head>
<meta charset="utf-8">
<title>Verdalia – Foam Car Wash Signage</title>
<link rel="stylesheet" href="https://fonts.googleapis.com/css2?family=Montserrat:wght@500;600;700;800;900&display=swap">
<style>
  :root {
    --backdrop: #231f20;
    --lime: #b8c941;
    --teal: #6fc1a1;
    --teal-deep: #4a9479;
    --ink: #111111;
    --panel: #ffffff;
    --mist-light: #f2f2f2;
    --mist-dark: #d6d6d6;
  }
  * { box-sizing: border-box; margin: 0; padding: 0; }
  html, body {
    width: 1200px; height: 1200px; overflow: hidden;
    background: var(--backdrop);
    font-family: "Montserrat", sans-serif;
  }
  .canvas { position: relative; width: 1200px; height: 1200px; }

  .sign {
    position: absolute;
    background: var(--panel);
    overflow: hidden;
    display: flex;
    flex-direction: column;
    align-items: center;
    justify-content: center;
  }
  .sign-corners { position: absolute; inset: 0; width: 100%; height: 100%; }
  .sign-content { position: relative; display: flex; flex-direction: column; align-items: center; }

  .brand { display: flex; align-items: center; gap: 18px; color: var(--lime); font-weight: 700; letter-spacing: 0.04em; line-height: 1; }
  .brand-dot { border-radius: 50%; background: var(--lime); flex: none; }

  /* Sign 1 – product statement */
  .sign--statement { left: 284px; top: 47px; width: 632px; height: 316px; }
  .sign--statement .mist {
    position: absolute; inset: 0;
    background: radial-gradient(circle at 40% 40%, var(--mist-light), var(--mist-dark));
  }
  .sign--statement .brand { font-size: 66px; margin-top: 6px; }
  .sign--statement .brand-dot { width: 44px; height: 44px; }
  .statement-lead {
    margin-top: 30px; text-align: center; color: var(--teal-deep);
    font-weight: 900; font-size: 24px; line-height: 1.1; letter-spacing: -0.02em;
  }
  .statement-products {
    margin-top: 14px; padding: 4px 2px 3px;
    border-top: 1.5px solid var(--ink); border-bottom: 1.5px solid var(--ink);
    color: var(--ink); font-weight: 700; font-size: 17px; letter-spacing: 0.12em;
  }

  /* Sign 2 – direction */
  .sign--direction { left: 325px; top: 407px; width: 549px; height: 274px; }
  .sign--direction .brand { font-size: 58px; }
  .sign--direction .brand-dot { width: 38px; height: 38px; }
  .direction-row { display: flex; align-items: center; gap: 10px; margin-top: 32px; }
  .petals { display: flex; gap: 2px; }
  .petal { width: 36px; height: 36px; fill: var(--teal); }
  .direction-label { color: var(--ink); font-weight: 700; font-size: 33px; letter-spacing: 0.01em; }

  /* Sign 3 – wash bay */
  .sign--bay { left: 185px; top: 722px; width: 829px; height: 207px; }
  .sign--bay .brand { font-size: 74px; }
  .sign--bay .brand-dot { width: 48px; height: 48px; }
  .bay-label { margin-top: 22px; color: var(--teal-deep); font-weight: 800; font-size: 36px; letter-spacing: 0.16em; }

  /* Sign 4 – facility front */
  .sign--front { left: 45px; top: 986px; width: 1110px; height: 148px; flex-direction: row; }
  .front-row { position: relative; display: flex; align-items: center; }
  .sign--front .brand { font-size: 72px; }
  .sign--front .brand-dot { width: 48px; height: 48px; }
  .front-divider { width: 1.5px; height: 110px; background: var(--teal); margin: 0 20px 0 28px; }
  .front-label { color: var(--teal); font-weight: 700; font-size: 40px; letter-spacing: -0.01em; }
</style>
</head>
<body>
<main class="canvas">

  <section class="sign sign--statement">
    <div class="mist" role="img" aria-label="Soft background of white foam bubbles"></div>
    <svg class="sign-corners" viewBox="0 0 632 316" preserveAspectRatio="none" aria-hidden="true">
      <polygon points="0,0 68,0 0,74" fill="var(--teal)"/>
      <polygon points="68,0 118,0 0,131 0,74" fill="var(--lime)"/>
      <polygon points="632,316 565,316 632,240" fill="var(--teal)"/>
      <polygon points="565,316 514,316 632,184 632,240" fill="var(--lime)"/>
    </svg>
    <div class="sign-content">
      <div class="brand"><span class="brand-dot"></span>VERDALIA</div>
      <p class="statement-lead">PREMIUM, ENVIRONMENT-FRIENDLY<br>BIODEGRADABLE</p>
      <p class="statement-products">FOAM WASH AND CLEANING PRODUCTS</p>
    </div>
  </section>

  <section class="sign sign--direction">
    <svg class="sign-corners" viewBox="0 0 549 274" preserveAspectRatio="none" aria-hidden="true">
      <polygon points="0,0 47,0 0,50" fill="var(--teal)"/>
      <polygon points="47,0 109,0 0,121 0,50" fill="var(--lime)"/>
      <polygon points="549,274 500,274 549,221" fill="var(--teal)"/>
      <polygon points="500,274 438,274 549,152 549,221" fill="var(--lime)"/>
    </svg>
    <div class="sign-content">
      <div class="brand"><span class="brand-dot"></span>VERDALIA</div>
      <div class="direction-row">
        <div class="petals" aria-hidden="true">
          <svg class="petal" viewBox="0 0 36 36"><path d="M1 18 Q1 12 9 8 L27 1 Q35 -1 35 8 V28 Q35 37 27 35 L9 28 Q1 24 1 18Z"/></svg>
          <svg class="petal" viewBox="0 0 36 36"><path d="M1 18 Q1 12 9 8 L27 1 Q35 -1 35 8 V28 Q35 37 27 35 L9 28 Q1 24 1 18Z"/></svg>
          <svg class="petal" viewBox="0 0 36 36"><path d="M1 18 Q1 12 9 8 L27 1 Q35 -1 35 8 V28 Q35 37 27 35 L9 28 Q1 24 1 18Z"/></svg>
        </div>
        <span class="direction-label">FOAM CAR WASH</span>
      </div>
    </div>
  </section>

  <section class="sign sign--bay">
    <svg class="sign-corners" viewBox="0 0 829 207" preserveAspectRatio="none" aria-hidden="true">
      <polygon points="0,0 70,0 0,76" fill="var(--teal)"/>
      <polygon points="70,0 121,0 0,135 0,76" fill="var(--lime)"/>
      <polygon points="829,207 758,207 829,129" fill="var(--teal)"/>
      <polygon points="758,207 706,207 829,71 829,129" fill="var(--lime)"/>
    </svg>
    <div class="sign-content">
      <div class="brand"><span class="brand-dot"></span>VERDALIA</div>
      <p class="bay-label">WASH BAY</p>
    </div>
  </section>

  <section class="sign sign--front">
    <svg class="sign-corners" viewBox="0 0 1110 148" preserveAspectRatio="none" aria-hidden="true">
      <polygon points="0,0 66,0 0,70" fill="var(--teal)"/>
      <polygon points="66,0 114,0 0,125 0,70" fill="var(--lime)"/>
      <polygon points="1110,148 1045,148 1110,76" fill="var(--teal)"/>
      <polygon points="1045,148 996,148 1110,22 1110,76" fill="var(--lime)"/>
    </svg>
    <div class="front-row">
      <div class="brand"><span class="brand-dot"></span>VERDALIA</div>
      <span class="front-divider"></span>
      <span class="front-label">FOAM CAR WASH</span>
    </div>
  </section>

</main>
</body>
</html>
```